Brennick Holdings Business Cards

These are professional business cards that are for my family office.
Put fake emails and phone numbers as of now until I finalize those components. This family office controls my families investments, assets, and future. The cards should be professional.
..
.
.
.
I just uploaded another variation of a logo I would like to see as a business card to I am inbeteen which logo to use

Target Market(s)

business

Industry/Entity Type

business

Contact Information for Business Card

Professional, wealth related, finance related.

Requirements
Must have
• Logo

```html
<!DOCTYPE html>
<html lang="en">
<head>
<meta charset="utf-8">
<title>Brennick Holdings Business Cards</title>
<link rel="stylesheet" href="https://fonts.googleapis.com/css2?family=Cinzel:wght@600&family=Open+Sans:wght@700&display=swap">
<style>
  :root {
    --page: #e6e5e3;
    --navy-top: #252c45;
    --navy-mid: #1b2030;
    --navy-bottom: #07080c;
    --ink: #1a1d29;
    --paper: #ffffff;
    --paper-shade: #eceef1;
    --dot: #b4b4b4;
    --dot-light: #d3d3d3;
  }
  * { margin: 0; padding: 0; box-sizing: border-box; }
  html, body { width: 1200px; height: 1200px; overflow: hidden; background: var(--page); }
  .canvas { position: relative; width: 1200px; height: 1200px; }

  .card {
    position: absolute;
    left: 210px;
    width: 780px;
    height: 444px;
    box-shadow: 0 6px 18px rgba(0,0,0,0.25);
    overflow: hidden;
  }

  /* Front */
  .card-front { top: 140px; }
  .front-field {
    position: absolute; inset: 0;
    background: linear-gradient(180deg, var(--navy-top) 0%, var(--navy-mid) 40%, var(--navy-bottom) 100%);
  }
  .name-band {
    position: absolute; left: 0; top: 156px; width: 100%; height: 131px;
    background: radial-gradient(ellipse at 50% 40%, #dadbdd 0%, var(--paper) 45%);
  }
  .front-name {
    position: absolute; left: 0; right: 0; top: 50px;
    text-align: center;
    font-family: "Cinzel", serif; font-weight: 600;
    font-size: 44px; letter-spacing: 1px;
    color: var(--ink);
  }
  .dot-row { position: absolute; display: flex; }
  .dot-row span { display: block; border-radius: 50%; }
  .front-dots { right: 82px; top: 22px; gap: 6px; }
  .front-dots span { width: 14px; height: 14px; background: var(--dot); }

  /* Back */
  .card-back { top: 650px; }
  .back-field {
    position: absolute; inset: 0;
    background: linear-gradient(160deg, var(--paper) 0%, var(--paper-shade) 55%, var(--paper) 100%);
  }
  .brand-block {
    position: absolute; left: 0; top: 0; width: 392px; height: 100%;
  }
  .brand-circle {
    position: absolute; left: 120px; top: 80px;
    width: 176px; height: 176px;
    border: 3px solid var(--ink); border-radius: 50%;
  }
  .back-name {
    position: absolute; left: 0; right: 0; top: 282px;
    text-align: center;
    font-family: "Cinzel", serif; font-weight: 600;
    font-size: 22px; color: var(--ink);
  }
  .divider {
    position: absolute; left: 392px; top: 95px; width: 1px; height: 285px;
    background: linear-gradient(180deg, rgba(0,0,0,0), rgba(0,0,0,0.12), rgba(0,0,0,0));
  }
  .contact-list { position: absolute; left: 449px; top: 0; list-style: none; }
  .contact-item { position: absolute; left: 0; display: flex; align-items: center; width: 320px; }
  .contact-icon {
    width: 44px; height: 44px; border-radius: 50%;
    background: var(--ink); flex: none;
    display: flex; align-items: center; justify-content: center;
  }
  .contact-text {
    margin-left: 13px;
    font-family: "Open Sans", sans-serif; font-weight: 700;
    font-size: 12.5px; line-height: 17px; color: var(--ink);
  }
  .item-email { top: 68px; }
  .item-phone { top: 135px; }
  .item-address { top: 207px; }
  .item-web { top: 274px; }
  .back-dots { right: 50px; top: 388px; gap: 7px; }
  .back-dots span { width: 17px; height: 17px; background: var(--dot-light); }
</style>
</head>
<body>
<main class="canvas">

  <section class="card card-front" aria-label="Business card front">
    <div class="front-field" role="img" aria-label="Dark navy field with subtle diamond pattern"></div>
    <div class="name-band">
      <div class="dot-row front-dots"><span></span><span></span><span></span><span></span><span></span></div>
      <h1 class="front-name">BRENNICK HOLDINGS</h1>
    </div>
  </section>

  <section class="card card-back" aria-label="Business card back">
    <div class="back-field" role="img" aria-label="Light field with subtle diamond pattern"></div>

    <div class="brand-block">
      <div class="brand-circle"></div>
      <p class="back-name">BRENNICK HOLDINGS</p>
    </div>

    <div class="divider"></div>

    <ul class="contact-list">
      <li class="contact-item item-email">
        <span class="contact-icon">
          <svg width="22" height="16" viewBox="0 0 22 16"><rect x="1" y="1" width="20" height="14" fill="none" stroke="#fff" stroke-width="1.6"/><path d="M1 1 L11 9 L21 1 M1 15 L8 7 M21 15 L14 7" fill="none" stroke="#fff" stroke-width="1.6"/></svg>
        </span>
        <span class="contact-text">INFO@COMPANY-NAME</span>
      </li>
      <li class="contact-item item-phone">
        <span class="contact-icon">
          <svg width="20" height="20" viewBox="0 0 24 24"><path d="M6.6 10.8c1.4 2.8 3.8 5.1 6.6 6.6l2.2-2.2c.3-.3.7-.4 1-.2 1.1.4 2.3.6 3.6.6.6 0 1 .4 1 1V20c0 .6-.4 1-1 1C10.6 21 3 13.4 3 4c0-.6.4-1 1-1h3.5c.6 0 1 .4 1 1 0 1.3.2 2.5.6 3.6.1.3 0 .7-.2 1z" fill="#fff"/></svg>
        </span>
        <span class="contact-text">+01 2345 6789 0123<br>+09 8765 4321 0987</span>
      </li>
      <li class="contact-item item-address">
        <span class="contact-icon">
          <svg width="24" height="22" viewBox="0 0 24 22"><path d="M12 1 L1 11 L4 11 L4 21 L10 21 L10 15 L14 15 L14 21 L20 21 L20 11 L23 11 Z" fill="#fff"/></svg>
        </span>
        <span class="contact-text">YOUR CITY ADDRESS<br>STREET LOCATION, STATE, COUNTRY</span>
      </li>
      <li class="contact-item item-web">
        <span class="contact-icon">
          <svg width="22" height="22" viewBox="0 0 22 22"><circle cx="11" cy="11" r="9.5" fill="none" stroke="#fff" stroke-width="1.6"/><ellipse cx="11" cy="11" rx="4" ry="9.5" fill="none" stroke="#fff" stroke-width="1.4"/><path d="M1.5 11 H20.5 M3.5 6 H18.5 M3.5 16 H18.5" stroke="#fff" stroke-width="1.2"/></svg>
        </span>
        <span class="contact-text">WWW.YOUR-COMPANY-NAME</span>
      </li>
    </ul>

    <div class="dot-row back-dots"><span></span><span></span><span></span><span></span><span></span></div>
  </section>

</main>
</body>
</html>
```